I would like a stylish low key card that represents my Cedar Nook. A boutique rental property . This property is of the highest standard and I wish the card to covey this without being old fashion

Boutique

Tessa Varrow
0427350192
tessa.varrow@varrow.com.au Cedar Nook

```html
<!DOCTYPE html>
<html lang="en">
<head>
<meta charset="utf-8">
<title>Cedar Nook – Business Card</title>
<link rel="stylesheet" href="https://fonts.googleapis.com/css2?family=Barlow:wght@300;400;600&display=swap">
<style>
  :root {
    --backdrop: #d4d4d4;
    --card-navy: #1e3158;
    --card-navy-deep: #17284a;
    --panel-navy: #15213a;
    --text-pale: #d3dfec;
    --text-soft: #b9c9db;
  }
  * { margin: 0; padding: 0; box-sizing: border-box; }
  html, body {
    width: 1200px;
    height: 741px;
    overflow: hidden;
    background: var(--backdrop);
    font-family: "Barlow", sans-serif;
  }
  .canvas {
    position: relative;
    width: 1200px;
    height: 741px;
  }
  .business-card {
    position: absolute;
    left: 120px;
    top: 92px;
    width: 960px;
    height: 556px;
    overflow: hidden;
  }
  .damask-field {
    position: absolute;
    inset: 0;
    background: radial-gradient(ellipse at 40% 40%, var(--card-navy) 0%, var(--card-navy-deep) 100%);
  }
  .contact-panel {
    position: absolute;
    left: 447px;
    top: 184px;
    width: 428px;
    bottom: 0;
    background: var(--panel-navy);
    padding: 22px 33px 0;
    color: var(--text-pale);
  }
  .contact-line {
    display: flex;
    gap: 28px;
    font-size: 25px;
    letter-spacing: 0.3px;
    line-height: 1.2;
  }
  .contact-name {
    font-weight: 600;
    text-transform: uppercase;
  }
  .contact-phone,
  .contact-email {
    font-weight: 400;
    color: var(--text-soft);
  }
  .contact-email {
    display: block;
    margin-top: 11px;
    font-size: 25px;
    letter-spacing: 0.3px;
  }
  .brand-name {
    position: absolute;
    left: 33px;
    bottom: 42px;
    font-size: 68px;
    font-weight: 300;
    color: var(--text-pale);
    letter-spacing: 0.5px;
    line-height: 1;
    white-space: nowrap;
  }
</style>
</head>
<body>
  <main class="canvas">
    <section class="business-card">
      <div class="damask-field" role="img" aria-label="Dark navy damask wallpaper pattern"></div>
      <div class="contact-panel">
        <p class="contact-line">
          <span class="contact-name">Tessa Varrow</span>
          <span class="contact-phone">042 735 01 92</span>
        </p>
        <span class="contact-email">tessa.varrow@varrow.com.au</span>
        <p class="brand-name">Cedar Nook</p>
      </div>
    </section>
  </main>
</body>
</html>
```